Desktop publishing rework of financial advisor's corporate marketing brochure

We are a financial and strategic business consultancy to corporate clients in healthcare/ pharmaceuticals. We previously had a very "wordy" slide presentation which we now thinned down to a few messages. We have created mockups of the layouts for the pages. We have also 95% finalized all wording for the pages. What we need is redesign proposals for all of the pages 1, 2, 4, 5, 6. These proposals should reflect the current layout/ arrangement of objects; they should be much more professional and generally "better looking" than what we currently have. They shall replace existing graphics with better-looking more appropriate ones.
Many thanks all

Requirements
Must have
• Use the PPT file shared below as basis

```html
<!DOCTYPE html>
<html lang="en">
<head>
<meta charset="utf-8">
<title>Ashcombe Partners – Brochure Pages</title>
<link rel="stylesheet" href="https://fonts.googleapis.com/css2?family=Rubik:wght@500;600;700&family=Poppins:wght@400;500;600;700&display=swap">
<style>
:root{
  --board:#dcdcdc;
  --paper:#f2f2f2;
  --navy:#0b0f7a;
  --blue:#17ace6;
  --sky:#3fd0f2;
  --ink:#141414;
  --grey:#9a9a9a;
  --foot:#1e1e1e;
}
*{box-sizing:border-box;margin:0;padding:0}
html,body{width:905px;height:1200px;overflow:hidden;background:var(--board)}
body{position:relative;font-family:"Poppins",sans-serif;color:var(--ink)}
.slide{position:absolute;width:387px;height:290px;overflow:hidden;
  background:linear-gradient(120deg,#fafafa 0%,#ececec 35%,#f8f8f8 55%,#e9e9e9 80%,#f6f6f6 100%);
  border-bottom:5px solid var(--foot);box-shadow:0 4px 10px rgba(0,0,0,.18)}
.s1{left:40px;top:104px}.s2{left:477px;top:104px}
.s3{left:40px;top:479px}.s4{left:477px;top:479px}.s5{left:259px;top:838px}
.abs{position:absolute}
.kicker{position:absolute;left:0;width:100%;text-align:center;font-family:"Rubik",sans-serif;font-weight:500;color:var(--ink);letter-spacing:-.2px}
.headline{position:absolute;left:0;width:100%;text-align:center;font-family:"Rubik",sans-serif;font-weight:700;color:var(--blue);letter-spacing:-.3px}
.divider{position:absolute;left:56px;width:275px;height:1px;background:#8a8a8a}
.divider::after{content:"";position:absolute;left:50%;top:-2px;width:38px;height:4px;margin-left:-19px;border-radius:2px;background:var(--blue)}

/* stat badges */
.badge{position:absolute;width:84px;height:86px}
.badge svg{position:absolute;inset:0}
.badge .num{position:absolute;top:2px;width:100%;text-align:center;color:#fff;font-weight:700;font-size:9px}
.badge .icon{position:absolute;top:24px;left:34px}
.badge .label{position:absolute;top:40px;width:100%;text-align:center;font-weight:600;font-size:8.4px;line-height:10.5px}

/* expertise wall */
.s2{background:linear-gradient(135deg,#2aa6e8 0%,#1aa4e4 45%,#3bd6f3 100%)}
.s2 .title1{position:absolute;left:14px;top:13px;font-family:"Rubik",sans-serif;font-weight:600;color:#fff;font-size:14px}
.s2 .title2{position:absolute;left:14px;top:28px;font-family:"Rubik",sans-serif;font-weight:700;color:var(--navy);font-size:19.5px}
.firm-name{position:absolute;right:16px;top:21px;color:#fff;font-family:"Poppins",sans-serif;font-weight:600;font-size:14px;line-height:16px}
.wall{position:absolute;left:15px;top:53px;width:357px;height:222px;border-radius:8px;background:#fff;padding:8px 8px}
.wall-row{display:flex;justify-content:space-between;align-items:center;height:20.4px;font-size:6.4px;color:var(--grey);font-weight:500;white-space:nowrap}
.wall-row .gap{width:104px;flex:none}
.wall-center{position:absolute;left:124px;top:102px;width:110px;text-align:center;font-family:"Poppins",sans-serif;font-weight:600;font-size:10.5px;color:#333;line-height:13px}
.wall svg{position:absolute;left:0;top:0}

/* approach */
.pill{position:absolute;height:22px;border-radius:8px;background:var(--blue);color:#fff;font-size:6.8px;font-weight:600;line-height:8px;text-align:center;display:flex;align-items:center;justify-content:center}
.venn-label{position:absolute;font-size:7px;font-weight:600;color:#fff}
.output-label{position:absolute;left:198px;top:207px;font-family:"Rubik",sans-serif;font-weight:600;color:var(--blue);font-size:9px;line-height:11px}

/* insight */
.tile{position:absolute;top:101px;width:80px;height:66px;border-radius:6px;background:var(--blue);overflow:hidden}
.tile-photo{background:linear-gradient(135deg,#7fb2d8 0%,#3a5a64 50%,#b3876a 100%)}
.tile-caption{position:absolute;top:177px;width:100px;text-align:center;font-size:7px;font-weight:600;line-height:8.4px}
.baseline{position:absolute;left:37px;width:312px;border-radius:8px;background:var(--navy);display:flex;align-items:center;overflow:hidden;box-shadow:0 6px 8px -4px rgba(0,0,0,.35)}
.baseline .tag{height:100%;width:66px;background:var(--blue);color:#fff;font-family:"Rubik",sans-serif;font-weight:600;font-size:9.5px;display:flex;align-items:center;justify-content:center;letter-spacing:.3px}
.baseline .claim{flex:1;text-align:center;color:#fff;font-family:"Rubik",sans-serif;font-weight:600;font-size:8.2px;letter-spacing:.2px}

/* areas */
.areas-art{position:absolute}
.areas-label{position:absolute;font-size:6.5px;font-weight:600;color:#444}
.areas-caption{position:absolute;top:210px;width:110px;text-align:center;font-size:6.5px;font-weight:600;line-height:8px}
.areas-caption b{color:var(--navy)}
.head-art{position:absolute;left:164px;top:106px;width:60px;height:65px;border-radius:30px 30px 10px 16px;background:linear-gradient(135deg,#1e2d6b 0%,#1aa4e4 50%,#9a9a9a 100%)}
</style>
</head>
<body>

<!-- Page 1 -->
<section class="slide s1">
  <p class="kicker" style="top:16px;font-size:14px">HEALTHCARE-FOCUSED ADVISOR FOUNDED BY</p>
  <h1 class="headline" style="top:31px;font-size:19.5px">FORMER NORTHGATE TEAM</h1>
  <div class="divider" style="top:60px"></div>

  <svg width="0" height="0" style="position:absolute">
    <defs>
      <symbol id="badge-shape" viewBox="0 0 84 86">
        <polygon points="10,62 42,76 74,62 74,74 42,86 10,74" fill="#0b0f7a"/>
        <polygon points="3,6 81,6 81,62 42,80 3,62" fill="#fff" stroke="#17ace6" stroke-width="1.3"/>
        <polygon points="8,0 76,0 76,10 42,22 8,10" fill="#0b0f7a"/>
      </symbol>
    </defs>
  </svg>

  <div class="badge" style="left:33px;top:77px"><svg viewBox="0 0 84 86"><use href="#badge-shape"/></svg><span class="num">15</span>
    <svg class="icon" width="15" height="14" viewBox="0 0 14 13"><circle cx="7" cy="3.5" r="2.6" fill="none" stroke="#222" stroke-width="1"/><path d="M2 12.5 V9.5 Q7 5 12 9.5 V12.5" fill="none" stroke="#222" stroke-width="1"/></svg>
    <p class="label">Senior<br>Professionals</p></div>
  <div class="badge" style="left:151px;top:77px"><svg viewBox="0 0 84 86"><use href="#badge-shape"/></svg><span class="num">&gt;$150BN</span>
    <svg class="icon" width="15" height="14" viewBox="0 0 14 13"><polygon points="4,1 10,1 12,4 7,9 2,4" fill="none" stroke="#222" stroke-width="1"/><path d="M1 12 H9 L13 9" fill="none" stroke="#222" stroke-width="1"/></svg>
    <p class="label">Transacted<br>Deal Value</p></div>
  <div class="badge" style="left:268px;top:77px"><svg viewBox="0 0 84 86"><use href="#badge-shape"/></svg><span class="num">15</span>
    <svg class="icon" width="15" height="14" viewBox="0 0 14 13"><rect x="2" y="1" width="10" height="7" fill="none" stroke="#222" stroke-width="1"/><path d="M1 12 H13 M4 8 V12 M10 8 V12" stroke="#222" stroke-width="1"/></svg>
    <p class="label">CEO Posts<br>Held</p></div>

  <div class="badge" style="left:33px;top:178px"><svg viewBox="0 0 84 86"><use href="#badge-shape"/></svg><span class="num">25YRS</span>
    <svg class="icon" width="15" height="14" viewBox="0 0 14 13"><circle cx="7" cy="6.5" r="5.5" fill="none" stroke="#222" stroke-width="1"/><path d="M7 3 V6.5 L9.5 8" fill="none" stroke="#222" stroke-width="1"/></svg>
    <p class="label">Average<br>Experience</p></div>
  <div class="badge" style="left:151px;top:178px"><svg viewBox="0 0 84 86"><use href="#badge-shape"/></svg><span class="num">&gt;100</span>
    <svg class="icon" width="15" height="14" viewBox="0 0 14 13"><circle cx="5" cy="5" r="3.5" fill="none" stroke="#222" stroke-width="1"/><circle cx="9.5" cy="8.5" r="3.5" fill="none" stroke="#222" stroke-width="1"/></svg>
    <p class="label">Individual<br>Transactions</p></div>
  <div class="badge" style="left:268px;top:178px"><svg viewBox="0 0 84 86"><use href="#badge-shape"/></svg><span class="num">&gt;20</span>
    <svg class="icon" width="15" height="14" viewBox="0 0 14 13"><rect x="3" y="1" width="8" height="5" fill="none" stroke="#222" stroke-width="1"/><path d="M7 6 V9 M2 12 L7 9 L12 12" fill="none" stroke="#222" stroke-width="1"/></svg>
    <p class="label">C-Suite<br>Positions Held</p></div>
</section>

<!-- Page 2 -->
<section class="slide s2">
  <p class="title1">DEEP COMPLEMENTARY</p>
  <h1 class="title2">SENIOR EXPERTISE</h1>
  <p class="firm-name">Ashcombe Partners</p>

  <div class="wall">
    <div class="wall-row"><span>Harlow Vance Group</span><span>Pellamy Capital</span><span>Corvell Bank</span><span>Ashby Rourke</span><span>Trenholm &amp; Co</span><span>Nuvexa</span></div>
    <div class="wall-row"><span>Quenby Bank</span><span>Lurwick</span><span>Falmere Group</span><span>Calder Reach</span><span>Morvane</span><span>Oxlyne</span><span>Peltram</span></div>
    <div class="wall-row"><span>Vessori</span><span>Tavix Bio</span><span>Ilmaren</span><span>Cordwell Trust</span><span>Brisen</span><span>Halvard Labs</span></div>
    <div class="wall-row"><span>Quintaro</span><span>Drexfield</span><span>Solmira</span><span class="gap"></span><span>ombrelix</span><span>Varnetta</span><span>Ellmoor Medical</span></div>
    <div class="wall-row"><span>iota-kem</span><span>prismelt.ai</span><span class="gap"></span><span>Tallowbrook Health</span><span>ovrenta</span></div>
    <div class="wall-row"><span>Kelvara Pharma</span><span>lumisca</span><span>rovantel</span><span class="gap"></span><span>Wystan Biosciences</span><span>nerivax</span></div>
    <div class="wall-row"><span>geniora</span><span>Fexolin</span><span>Ardent Vale Care</span><span>imbrela</span><span>Peptorra</span><span>Ferncliff Health</span></div>
    <div class="wall-row"><span>Zyphera</span><span>Cantorel</span><span>Marrowind Therapeutics</span><span>cellastra</span><span>Q.V.L.</span></div>
    <div class="wall-row"><span>HVU</span><span>Synaptrel</span><span>Orphenne</span><span>Thistle Therapeutics</span><span>Quiet Harbor Therapeutics</span></div>
    <div class="wall-row"><span>Epivane</span><span>Tesselbio</span><span>Mavrina</span><span>Lyxora</span><span>CellKite</span><span>Orvelle</span></div>

    <svg width="357" height="222" viewBox="0 0 357 222">
      <g fill="none" stroke="#17ace6" stroke-width="1.6">
        <path d="M138 80 Q140 95 160 97"/>
        <path d="M246 83 Q232 86 226 97"/>
        <path d="M180 155 Q196 152 200 124"/>
      </g>
      <g fill="#17ace6">
        <polygon points="160,94 165,97 160,100"/>
        <polygon points="223,95 229,95 226,100"/>
        <polygon points="197,125 203,125 200,120"/>
      </g>
    </svg>
    <p class="wall-center">Ashcombe Partners</p>
  </div>
</section>

<!-- Page 3 -->
<section class="slide s3">
  <p class="kicker" style="top:14px;font-size:14px">UNIQUE APPROACH TO DELIVERING</p>
  <h1 class="headline" style="top:28px;font-size:19.5px">CLIENT SUCCESS</h1>
  <div class="divider" style="top:54px"></div>

  <div class="pill" style="left:42px;top:77px;width:108px">Seamless Integration<br>of Disciplines</div>
  <div class="pill" style="left:253px;top:77px;width:108px">Successful Transactions<br>&amp; Corporate Evolutions</div>

  <svg class="abs" style="left:0;top:100px" width="387" height="150" viewBox="0 0 387 150">
    <defs>
      <linearGradient id="chev" x1="0" x2="1"><stop offset="0" stop-color="#c7c7c7"/><stop offset="1" stop-color="#f0f0f0"/></linearGradient>
      <radialGradient id="core" cx="0.5" cy="0.5" r="0.5"><stop offset="0.55" stop-color="#6c8fd8"/><stop offset="0.8" stop-color="#2ab0ec"/><stop offset="1" stop-color="#9fdcf6"/></radialGradient>
    </defs>
    <polygon points="158,70 186,102 158,134 168,102" fill="url(#chev)"/>
    <circle cx="91" cy="52" r="38" fill="#17ace6"/>
    <circle cx="65" cy="102" r="38" fill="#0b0f7a"/>
    <circle cx="121" cy="102" r="38" fill="#9b9b9b"/>
    <polygon points="91,64 110,98 72,98" fill="#fff"/>
    <circle cx="91" cy="64" r="11" fill="#fff" stroke="#ddd"/>
    <circle cx="66" cy="98" r="11" fill="#fff" stroke="#ddd"/>
    <circle cx="120" cy="98" r="11" fill="#fff" stroke="#ddd"/>
    <g fill="none" stroke="#222" stroke-width=".9">
      <circle cx="88" cy="62" r="3.5"/><circle cx="94" cy="66" r="3.5"/>
      <rect x="61" y="93" width="10" height="7"/><path d="M63 100 L61 104 M69 100 L71 104"/>
      <circle cx="120" cy="98" r="3"/><circle cx="120" cy="98" r="5.5" stroke-dasharray="2 1.5"/>
    </g>
    <line x1="194" y1="102" x2="266" y2="102" stroke="#17ace6" stroke-width=".8" stroke-dasharray="2 1.5"/>
    <polygon points="266,98 272,102 266,106" fill="#17ace6"/>
    <circle cx="315" cy="102" r="38" fill="#d6d6d6"/>
    <circle cx="315" cy="102" r="31" fill="#8f8f8f"/>
    <circle cx="315" cy="102" r="26" fill="#cfe9f7"/>
    <circle cx="315" cy="102" r="21" fill="url(#core)"/>
  </svg>
  <span class="venn-label" style="left:70px;top:127px">Transaction</span>
  <span class="venn-label" style="left:47px;top:216px">Strategy</span>
  <span class="venn-label" style="left:98px;top:216px">Management</span>
  <p class="output-label">CONSOLIDATED<br>OUTPUT</p>
</section>

<!-- Page 4 -->
<section class="slide s4">
  <p class="kicker" style="top:18px;font-size:9.5px">OUTSOURCED SOLUTION DELIVERY OFFICE FOR OUR CLIENTS</p>
  <h1 class="headline" style="top:30px;font-size:19.5px">ENHANCED INSIGHT</h1>
  <div class="divider" style="top:63px"></div>

  <div class="tile" style="left:37px">
    <svg width="80" height="66" viewBox="0 0 80 66"><g fill="none" stroke="#fff" stroke-width="3.2" stroke-linecap="round"><path d="M36 10 L44 26"/><path d="M47 30 Q56 42 44 50"/><path d="M24 52 H52"/><path d="M34 44 Q32 36 40 33"/></g></svg>
  </div>
  <div class="tile tile-photo" style="left:153px" role="img" aria-label="Photograph of hands holding binoculars against a blue sky"></div>
  <div class="tile" style="left:274px">
    <svg width="80" height="66" viewBox="0 0 80 66"><g fill="#fff"><circle cx="22" cy="22" r="8"/><path d="M8 56 Q8 34 22 34 Q36 34 36 56 Z"/></g><g fill="none" stroke="#fff" stroke-width="1"><path d="M46 33 H54 M54 22 V44 M54 22 H64 M54 44 H64 M60 22 V29 H68 M60 44 V37 H68"/></g><polygon points="42,33 46,30 46,36" fill="#fff"/></svg>
  </div>

  <p class="tile-caption" style="left:27px">UNDERSTAND<br>SITUATIONS</p>
  <p class="tile-caption" style="left:143px">IDENTIFY<br>DIRECTIONS</p>
  <p class="tile-caption" style="left:264px">INFORM<br>DECISION-MAKING</p>

  <div class="baseline" style="top:221px;height:24px"><span class="tag">BASELINE</span><span class="claim">FLAWLESS SUCCESSFUL EXECUTION THROUGHOUT</span></div>
</section>

<!-- Page 5 -->
<section class="slide s5">
  <p class="kicker" style="top:18px;font-size:9.5px">OUTSOURCED SOLUTION DELIVERY OFFICE</p>
  <h1 class="headline" style="top:29px;font-size:19.5px">AREAS OF WORK</h1>
  <div class="divider" style="top:60px"></div>

  <svg class="areas-art" style="left:12px;top:75px" width="136" height="123" viewBox="0 0 136 123">
    <defs>
      <linearGradient id="band-o" x1="0" x2="1"><stop offset="0" stop-color="#e0400a"/><stop offset=".5" stop-color="#ff7a1c"/><stop offset="1" stop-color="#e0400a"/></linearGradient>
      <linearGradient id="band-b" x1="0" x2="1"><stop offset="0" stop-color="#0f5fc8"/><stop offset=".5" stop-color="#2aa4ee"/><stop offset="1" stop-color="#0f5fc8"/></linearGradient>
      <linearGradient id="band-p" x1="0" x2="1"><stop offset="0" stop-color="#c9237a"/><stop offset=".5" stop-color="#f75aa8"/><stop offset="1" stop-color="#c9237a"/></linearGradient>
      <linearGradient id="band-l" x1="0" x2="1"><stop offset="0" stop-color="#b866d6"/><stop offset=".5" stop-color="#ee9cf3"/><stop offset="1" stop-color="#b866d6"/></linearGradient>
    </defs>
    <polygon points="0,0 136,0 119.4,30 16.6,30" fill="url(#band-o)"/>
    <polygon points="16.6,31 119.4,31 103.4,59 32.6,59" fill="url(#band-b)"/>
    <polygon points="32.6,60 103.4,60 89,85 47,85" fill="url(#band-p)"/>
    <polygon points="47,86 89,86 68,123" fill="url(#band-l)"/>
    <g fill="#fff" font-family="Rubik, sans-serif" font-weight="600" text-anchor="middle">
      <text x="68" y="19" font-size="9">IDENTIFY</text>
      <text x="68" y="49" font-size="9">SCREEN</text>
      <text x="68" y="76" font-size="7.5">REVIEW</text>
      <text x="68" y="96" font-size="3.5">TRANSACT</text>
    </g>
  </svg>

  <div class="head-art" role="img" aria-label="Illustration of a human head profile made of four interlocking puzzle pieces"></div>
  <span class="areas-label" style="left:152px;top:93px">Strategize</span>
  <span class="areas-label" style="left:212px;top:93px">Adjust</span>
  <span class="areas-label" style="left:152px;top:168px">Implement</span>
  <span class="areas-label" style="left:210px;top:168px">Monitor</span>

  <svg class="areas-art" style="left:241px;top:73px" width="136" height="122" viewBox="0 0 136 122">
    <polygon points="68,0 86.4,33 49.6,33" fill="url(#band-l)"/>
    <polygon points="49.6,34 86.4,34 102.6,62 33.4,62" fill="url(#band-p)"/>
    <polygon points="33.4,63 102.6,63 118.2,90 17.8,90" fill="url(#band-b)"/>
    <polygon points="17.8,91 118.2,91 136,122 0,122" fill="url(#band-o)"/>
    <g fill="#fff" font-family="Rubik, sans-serif" font-weight="600" text-anchor="middle">
      <text x="68" y="25" font-size="3.5">EXECUTE</text>
      <text x="68" y="52" font-size="7.5">APPROACH</text>
      <text x="68" y="80" font-size="8.5">PREPARE</text>
      <text x="68" y="110" font-size="9">PLAN</text>
    </g>
  </svg>

  <p class="areas-caption" style="left:23px"><b>Inward Transactions:</b><br>Buy | In-License | Partner<br>Invest</p>
  <p class="areas-caption" style="left:138px"><b>Senior Management:</b><br>Companies | Businesses<br>Portfolios | Products</p>
  <p class="areas-caption" style="left:254px"><b>Outward Transactions</b><br>Sell | Out-License | Partner<br>Re-Finance</p>

  <div class="baseline" style="top:245px;height:19px"><span class="tag">BASELINE</span><span class="claim">FLAWLESS SUCCESSFUL EXECUTION THROUGHOUT</span></div>
</section>

</body>
</html>
```